Breakthrough Medical Device to Prevent Life-Threatening Respiratory Infections

Design a 4 page brochure using color scheme of VolaGuard logo. The brochure is for an advanced endotracheal tube that is able to prevent bacterial and fungal growth on its surfaces after being placed inside the patient's trachea. Endotracheal tubes are necessary to provide air to patients who cannot breather on their own. However, within hours of placing the endotracheal tube in the patient, bacteria and fungi in the patient's airway colonize the tube and form biofilms -- slime like aggregations that are resistant to antibiotics. These biofilms can dislodge from the tube and go into the patient's lungs causing potentially deadly infections.

Target Market(s)

Hospitals, Physicians

Industry/Entity Type

Medical Equipment

Font styles to use
Sans Serif

Colors
0455a3
33a6d7
ffffff

Requirements
Must have
• iimage of endotracheal tube, graphs from document sent, language in word file appropriately placed

```html
<!DOCTYPE html>
<html lang="en">
<head>
<meta charset="utf-8">
<title>VolaGuard Endotracheal Tube Brochure Spread</title>
<link rel="stylesheet" href="https://fonts.googleapis.com/css2?family=Arimo:wght@400;700&family=Open+Sans:ital,wght@0,400;0,700;1,400;1,700&display=swap">
<style>
  :root{
    --navy:#0455a3;
    --sky:#33a6d7;
    --white:#ffffff;
    --backdrop:#c9d6dc;
    --ink:#1a1a1a;
    --bar-dark:#0b0b0b;
    --bar-grey:#c9c9c9;
    --page:#f8f8f8;
  }
  *{box-sizing:border-box;margin:0;padding:0}
  html,body{width:1200px;height:833px;overflow:hidden;background:var(--backdrop)}
  .canvas{position:relative;width:1200px;height:833px}
  .page{position:absolute;top:56px;width:560px;height:720px;background:var(--page);overflow:hidden}
  .page--left{left:40px;box-shadow:-2px 4px 14px rgba(0,0,0,.18)}
  .page--right{left:600px;box-shadow:2px 4px 14px rgba(0,0,0,.18)}
  .band{position:absolute;left:0;width:100%}
  .band--top{top:0;height:52px}
  .band--bottom{bottom:0;height:74px}
  .page--left .band--top{background:linear-gradient(90deg,var(--navy),var(--sky))}
  .page--left .band--bottom{background:linear-gradient(90deg,var(--sky),var(--navy))}
  .page--right .band--top{background:linear-gradient(90deg,var(--sky),var(--navy))}
  .page--right .band--bottom{background:linear-gradient(90deg,var(--navy),var(--sky))}
  .bullets{position:absolute;list-style:none;font-family:"Arimo",sans-serif;color:var(--ink)}
  .bullets li{position:relative;padding-left:16px;line-height:1.15}
  .bullets li::before{content:"";position:absolute;left:0;top:.45em;width:6px;height:6px;border-radius:50%;background:var(--sky)}
  .bullets--lead{left:22px;top:68px;font-size:15px}
  .bullets--lead li{margin-bottom:2px}
  .bullets--claims{left:14px;width:532px;font-size:14.5px}
  .bullets--claims li{margin-bottom:10px}
  .art{position:absolute;border-radius:4px}
  .art--molecule{left:30px;top:136px;width:320px;height:150px;background:linear-gradient(135deg,#eeeeee,#dcdcdc)}
  .art--tube{left:380px;top:66px;width:165px;height:230px;background:linear-gradient(160deg,#e9ecee,#cfd5d9)}
  .chart{position:absolute}
  .chart svg{width:100%;height:100%;display:block}
  .caption{position:absolute;font-family:"Open Sans",sans-serif;color:var(--ink);line-height:1.3}
  .caption b{font-style:italic}
  .caption--left{left:22px;top:566px;width:520px;font-size:7.4px}
  .caption--right{left:60px;width:450px;font-size:5.6px}
  .axis{stroke:var(--ink);stroke-width:.8;fill:none}
  .bar{fill:var(--bar-dark)}
  .bar--coated{fill:var(--bar-grey);stroke:var(--ink);stroke-width:.5}
  .err{stroke:var(--ink);stroke-width:.6}
  .tick{font-family:"Open Sans",sans-serif;font-size:6px;fill:var(--ink)}
  .panel{font-family:"Open Sans",sans-serif;font-size:8px;fill:var(--ink)}
</style>
</head>
<body>
<main class="canvas">

  <section class="page page--left">
    <div class="band band--top"></div>

    <ul class="bullets bullets--lead">
      <li>Passive device</li>
      <li>No need for subglottic suctioning</li>
      <li>No need for human intervention</li>
    </ul>

    <div class="art art--molecule" role="img" aria-label="Chemical structure of the antimicrobial coating compound"></div>
    <div class="art art--tube" role="img" aria-label="Coated endotracheal tube with cuff"></div>

    <div class="chart" style="left:14px;top:326px;width:170px;height:110px">
      <svg viewBox="0 0 160 104">
        <text class="panel" x="2" y="7">(a)</text>
        <text class="tick" transform="translate(7 62) rotate(-90)">Log cfu/mL</text>
        <path class="axis" d="M18 8V88H158"/>
        <text class="tick" x="12" y="90">0</text><text class="tick" x="12" y="63">3</text><text class="tick" x="12" y="37">6</text><text class="tick" x="12" y="10">9</text>
        <rect class="bar" x="27" y="21.3" width="7" height="66.7"/>
        <rect class="bar" x="62" y="27.6" width="7" height="60.4"/>
        <rect class="bar" x="97" y="16.9" width="7" height="71.1"/>
        <rect class="bar--coated" x="106" y="8" width="7" height="80"/>
        <rect class="bar" x="132" y="18.7" width="7" height="69.3"/>
        <rect class="bar--coated" x="141" y="54.2" width="7" height="33.8"/>
        <line class="err" x1="135.5" y1="11" x2="135.5" y2="18.7"/>
        <text class="tick" x="24" y="98">Day 5</text><text class="tick" x="59" y="98">Day 6</text><text class="tick" x="96" y="98">Day 7</text><text class="tick" x="131" y="98">Day 8</text>
      </svg>
    </div>
    <div class="chart" style="left:190px;top:316px;width:170px;height:110px">
      <svg viewBox="0 0 160 104">
        <text class="panel" x="2" y="7">(b)</text>
        <text class="tick" transform="translate(7 62) rotate(-90)">Log cfu/mL</text>
        <path class="axis" d="M18 8V88H158"/>
        <text class="tick" x="12" y="90">0</text><text class="tick" x="12" y="63">3</text><text class="tick" x="12" y="37">6</text><text class="tick" x="12" y="10">9</text>
        <rect class="bar" x="27" y="34.7" width="7" height="53.3"/>
        <rect class="bar" x="62" y="27.6" width="7" height="60.4"/>
        <rect class="bar" x="97" y="24" width="7" height="64"/>
        <rect class="bar" x="132" y="20.4" width="7" height="67.6"/>
        <rect class="bar--coated" x="141" y="77.3" width="7" height="10.7"/>
        <line class="err" x1="144.5" y1="64" x2="144.5" y2="77.3"/>
        <text class="tick" x="24" y="98">Day 5</text><text class="tick" x="59" y="98">Day 7</text><text class="tick" x="96" y="98">Day 8</text><text class="tick" x="131" y="98">Day 9</text>
      </svg>
    </div>
    <div class="chart" style="left:366px;top:316px;width:170px;height:110px">
      <svg viewBox="0 0 160 104">
        <text class="panel" x="2" y="7">(c)</text>
        <text class="tick" transform="translate(7 62) rotate(-90)">Log cfu/mL</text>
        <path class="axis" d="M18 8V88H158"/>
        <text class="tick" x="12" y="90">0</text><text class="tick" x="12" y="63">3</text><text class="tick" x="12" y="37">6</text><text class="tick" x="12" y="10">9</text>
        <rect class="bar" x="27" y="21.3" width="7" height="66.7"/>
        <rect class="bar" x="62" y="25.8" width="7" height="62.2"/>
        <rect class="bar" x="97" y="31.1" width="7" height="56.9"/>
        <rect class="bar--coated" x="106" y="83.6" width="7" height="4.4"/>
        <line class="err" x1="109.5" y1="70" x2="109.5" y2="83.6"/>
        <rect class="bar" x="132" y="34.7" width="7" height="53.3"/>
        <rect class="bar--coated" x="141" y="53.3" width="7" height="34.7"/>
        <text class="tick" x="24" y="98">Day 1</text><text class="tick" x="59" y="98">Day 2</text><text class="tick" x="96" y="98">Day 3</text><text class="tick" x="131" y="98">Day 4</text>
      </svg>
    </div>

    <div class="chart" style="left:96px;top:444px;width:170px;height:110px">
      <svg viewBox="0 0 160 104">
        <text class="panel" x="2" y="7">(d)</text>
        <text class="tick" transform="translate(7 62) rotate(-90)">Log cfu/mL</text>
        <path class="axis" d="M18 8V88H158"/>
        <text class="tick" x="12" y="90">0</text><text class="tick" x="12" y="70">2</text><text class="tick" x="12" y="50">4</text><text class="tick" x="12" y="30">6</text><text class="tick" x="12" y="10">8</text>
        <rect class="bar" x="27" y="38" width="7" height="50"/>
        <rect class="bar" x="62" y="23" width="7" height="65"/>
        <rect class="bar" x="97" y="28" width="7" height="60"/>
        <rect class="bar" x="132" y="15" width="7" height="73"/>
        <rect class="bar--coated" x="141" y="48" width="7" height="40"/>
        <line class="err" x1="144.5" y1="38" x2="144.5" y2="60"/>
        <text class="tick" x="24" y="98">Day 5</text><text class="tick" x="59" y="98">Day 7</text><text class="tick" x="96" y="98">Day 9</text><text class="tick" x="129" y="98">Day 16</text>
      </svg>
    </div>
    <div class="chart" style="left:272px;top:439px;width:170px;height:110px">
      <svg viewBox="0 0 160 104">
        <text class="panel" x="2" y="7">(e)</text>
        <text class="tick" transform="translate(7 62) rotate(-90)">Log cfu/mL</text>
        <path class="axis" d="M18 8V88H158"/>
        <text class="tick" x="12" y="90">0</text><text class="tick" x="12" y="70">2</text><text class="tick" x="12" y="50">4</text><text class="tick" x="12" y="30">6</text><text class="tick" x="12" y="10">8</text>
        <rect class="bar" x="27" y="16" width="7" height="72"/>
        <rect class="bar" x="62" y="19" width="7" height="69"/>
        <rect class="bar" x="97" y="25" width="7" height="63"/>
        <rect class="bar" x="132" y="25" width="7" height="63"/>
        <rect class="bar--coated" x="141" y="53" width="7" height="35"/>
        <line class="err" x1="144.5" y1="42" x2="144.5" y2="64"/>
        <text class="tick" x="24" y="98">Day 5</text><text class="tick" x="59" y="98">Day 6</text><text class="tick" x="96" y="98">Day 7</text><text class="tick" x="131" y="98">Day 8</text>
      </svg>
    </div>

    <p class="caption caption--left"><b>Figure 3.</b> Biofilms formed on ETT segments (5 mm) after the indicated number of days of incubation (daily exchange of growth medium and re-inoculation). Measurements were made in triplicate. Black bars, uncoated tube segments; grey bars, coated segments. (a) MRSA (BAA-41, 10⁶ cfu inoculation). (b) <i>K. pneumoniae</i> (ATCC 13883, 10⁶ cfu inoculation). (c) <i>P. aeruginosa</i> (ATCC 47085, 10⁶ cfu inoculation). (d) <i>C. albicans</i> (ATCC 90028, 10⁵ cfu inoculation). (e) <i>C. auris</i> (CDC 0383, 10⁵ cfu inoculation).</p>

    <div class="band band--bottom"></div>
  </section>

  <section class="page page--right">
    <div class="band band--top"></div>

    <ul class="bullets bullets--claims" style="top:64px">
      <li>Designed to Prevent bacterial and fungal colonization of all surfaces including the cuff</li>
      <li>Prevents biofilm growth and related endotoxins for clinically-relevant time periods</li>
    </ul>

    <div class="chart" style="left:70px;top:150px;width:130px;height:88px">
      <svg viewBox="0 0 160 104">
        <text class="panel" x="2" y="7">(a)</text>
        <path class="axis" d="M18 8V88H158"/>
        <rect class="bar" x="27" y="21.3" width="7" height="66.7"/><rect class="bar" x="62" y="27.6" width="7" height="60.4"/>
        <rect class="bar" x="97" y="16.9" width="7" height="71.1"/><rect class="bar--coated" x="106" y="8" width="7" height="80"/>
        <rect class="bar" x="132" y="18.7" width="7" height="69.3"/><rect class="bar--coated" x="141" y="54.2" width="7" height="33.8"/>
        <text class="tick" x="24" y="98">Day 5</text><text class="tick" x="59" y="98">Day 6</text><text class="tick" x="96" y="98">Day 7</text><text class="tick" x="131" y="98">Day 8</text>
      </svg>
    </div>
    <div class="chart" style="left:204px;top:152px;width:130px;height:88px">
      <svg viewBox="0 0 160 104">
        <text class="panel" x="2" y="7">(b)</text>
        <path class="axis" d="M18 8V88H158"/>
        <rect class="bar" x="27" y="34.7" width="7" height="53.3"/><rect class="bar" x="62" y="27.6" width="7" height="60.4"/>
        <rect class="bar" x="97" y="24" width="7" height="64"/><rect class="bar" x="132" y="20.4" width="7" height="67.6"/>
        <rect class="bar--coated" x="141" y="77.3" width="7" height="10.7"/>
        <text class="tick" x="24" y="98">Day 5</text><text class="tick" x="59" y="98">Day 7</text><text class="tick" x="96" y="98">Day 8</text><text class="tick" x="131" y="98">Day 9</text>
      </svg>
    </div>
    <div class="chart" style="left:338px;top:154px;width:130px;height:88px">
      <svg viewBox="0 0 160 104">
        <text class="panel" x="2" y="7">(c)</text>
        <path class="axis" d="M18 8V88H158"/>
        <rect class="bar" x="27" y="21.3" width="7" height="66.7"/><rect class="bar" x="62" y="25.8" width="7" height="62.2"/>
        <rect class="bar" x="97" y="31.1" width="7" height="56.9"/><rect class="bar--coated" x="106" y="83.6" width="7" height="4.4"/>
        <rect class="bar" x="132" y="34.7" width="7" height="53.3"/><rect class="bar--coated" x="141" y="53.3" width="7" height="34.7"/>
        <text class="tick" x="24" y="98">Day 1</text><text class="tick" x="59" y="98">Day 2</text><text class="tick" x="96" y="98">Day 3</text><text class="tick" x="131" y="98">Day 4</text>
      </svg>
    </div>
    <div class="chart" style="left:130px;top:242px;width:130px;height:88px">
      <svg viewBox="0 0 160 104">
        <text class="panel" x="2" y="7">(d)</text>
        <path class="axis" d="M18 8V88H158"/>
        <rect class="bar" x="27" y="38" width="7" height="50"/><rect class="bar" x="62" y="23" width="7" height="65"/>
        <rect class="bar" x="97" y="28" width="7" height="60"/><rect class="bar" x="132" y="15" width="7" height="73"/>
        <rect class="bar--coated" x="141" y="48" width="7" height="40"/>
        <text class="tick" x="24" y="98">Day 5</text><text class="tick" x="59" y="98">Day 7</text><text class="tick" x="96" y="98">Day 9</text><text class="tick" x="129" y="98">Day 16</text>
      </svg>
    </div>
    <div class="chart" style="left:264px;top:244px;width:130px;height:88px">
      <svg viewBox="0 0 160 104">
        <text class="panel" x="2" y="7">(e)</text>
        <path class="axis" d="M18 8V88H158"/>
        <rect class="bar" x="27" y="16" width="7" height="72"/><rect class="bar" x="62" y="19" width="7" height="69"/>
        <rect class="bar" x="97" y="25" width="7" height="63"/><rect class="bar" x="132" y="25" width="7" height="63"/>
        <rect class="bar--coated" x="141" y="53" width="7" height="35"/>
        <text class="tick" x="24" y="98">Day 5</text><text class="tick" x="59" y="98">Day 6</text><text class="tick" x="96" y="98">Day 7</text><text class="tick" x="131" y="98">Day 8</text>
      </svg>
    </div>

    <p class="caption caption--right" style="top:338px"><b>Figure 3.</b> Biofilms formed on ETT segments (5 mm) after the indicated number of days of incubation (daily exchange of growth medium and re-inoculation). Measurements were made in triplicate. Black bars, uncoated tube segments; grey bars, coated segments. (a) MRSA (BAA-41, 10⁶ cfu inoculation). (b) <i>K. pneumoniae</i> (ATCC 13883, 10⁶ cfu inoculation). (c) <i>P. aeruginosa</i> (ATCC 47085, 10⁶ cfu inoculation). (d) <i>C. albicans</i> (ATCC 90028, 10⁵ cfu inoculation). (e) <i>C. auris</i> (CDC 0383, 10⁵ cfu inoculation).</p>

    <div class="chart" style="left:140px;top:386px;width:140px;height:96px">
      <svg viewBox="0 0 160 104">
        <text class="panel" x="2" y="7">(a)</text>
        <text class="tick" transform="translate(7 62) rotate(-90)">Log cfu/mL</text>
        <path class="axis" d="M18 8V88H158"/>
        <rect class="bar" x="27" y="13" width="7" height="75"/>
        <rect class="bar" x="62" y="13" width="7" height="75"/><rect class="bar--coated" x="71" y="53" width="7" height="35"/>
        <rect class="bar" x="97" y="18" width="7" height="70"/><rect class="bar--coated" x="106" y="20" width="7" height="68"/>
        <rect class="bar" x="132" y="18" width="7" height="70"/><rect class="bar--coated" x="141" y="30" width="7" height="58"/>
        <text class="tick" x="24" y="98">Day 1</text><text class="tick" x="59" y="98">Day 2</text><text class="tick" x="96" y="98">Day 3</text><text class="tick" x="131" y="98">Day 4</text>
      </svg>
    </div>
    <div class="chart" style="left:290px;top:388px;width:140px;height:96px">
      <svg viewBox="0 0 160 104">
        <text class="panel" x="2" y="7">(b)</text>
        <text class="tick" transform="translate(7 62) rotate(-90)">Log cfu/mL</text>
        <path class="axis" d="M18 8V88H158"/>
        <rect class="bar" x="27" y="28" width="7" height="60"/>
        <rect class="bar" x="62" y="26" width="7" height="62"/>
        <rect class="bar" x="97" y="30" width="7" height="58"/><rect class="bar--coated" x="106" y="83" width="7" height="5"/>
        <rect class="bar" x="132" y="32" width="7" height="56"/><rect class="bar--coated" x="141" y="40" width="7" height="48"/>
        <text class="tick" x="24" y="98">Day 1</text><text class="tick" x="59" y="98">Day 2</text><text class="tick" x="96" y="98">Day 3</text><text class="tick" x="131" y="98">Day 4</text>
      </svg>
    </div>

    <p class="caption caption--right" style="top:490px"><b>Figure 4.</b> Mixed species biofilms formed on ETT segments (5 mm) after the indicated number of days of incubation (daily exchange of growth medium and re-inoculation). Measurements made in triplicate. Black bars: uncoated tube segments; gray bars: coated segments. (a) MRSA (BAA-41, 10⁶ cfu inoculation) with <i>P. aeruginosa</i> (ATCC 47085, 10⁶ cfu inoculation). (b) <i>P. aeruginosa</i> (ATCC 47085, 10⁶ cfu inoculation) with <i>C. auris</i> (CDC 0383, 10⁵ cfu inoculation).</p>

    <ul class="bullets bullets--claims" style="top:552px">
      <li>Contains broad spectrum antimicrobial and anti-inflammatory compound that slowly elutes from coating upon exposure to body fluids</li>
      <li>Highly lubricious coating reduces coefficient of friction by 30x</li>
    </ul>

    <div class="band band--bottom"></div>
  </section>

</main>
</body>
</html>
```